Flyer needed for a Summer Course

We need a flyer made for a summer course that will review a chapter of the Qur'an (holy book). The flyer can include imagery related to a table spread with delicious food outdoors in a garden setting, or any generic light/path to a garden or to light. Please include the attached logo to the flyer as well. The following information should be included in the flyer:
Tafsir of Surah Maidah
Taught by Delira Nasrim
June 1 to June 15 2017
Daily Monday thru Thursday
1:30 PM to 2:30 PM
Unity Hall of Brookvale Township
2400 Tarrow Road
Piscataway NJ 08617
For more information: sahelwing4@quorimail.com

```html
<!DOCTYPE html>
<html lang="en">
<head>
<meta charset="utf-8">
<title>Tafsir of Surah Maidah – Summer Course Flyer</title>
<link href="https://fonts.googleapis.com/css2?family=Pinyon+Script&family=Roboto:wght@700;900&display=swap" rel="stylesheet">
<style>
  :root {
    --leaf-deep: #2f4a12;
    --leaf: #6f9a22;
    --leaf-light: #b9d35a;
    --sun: #fffbe0;
    --autumn: #d99a2b;
    --autumn-deep: #8a4b12;
    --band: #0a0a0a;
    --white: #ffffff;
    --orange: #f07a12;
    --green-text: #35b84a;
    --title-edge: #1c1c1c;
  }
  html, body {
    margin: 0;
    padding: 0;
    width: 1200px;
    height: 850px;
    overflow: hidden;
    background: #ffffff;
  }
  .flyer {
    position: relative;
    width: 1200px;
    height: 850px;
    overflow: hidden;
    font-family: "Roboto", Arial, sans-serif;
  }
  .garden-scene {
    position: absolute;
    left: 0; top: 0;
    width: 1200px;
    height: 761px;
    background:
      radial-gradient(ellipse 260px 300px at 560px 380px, var(--sun) 0%, rgba(255,250,210,0.85) 30%, rgba(255,240,170,0) 100%),
      radial-gradient(ellipse 520px 180px at 560px 720px, rgba(224,160,50,0.9) 0%, rgba(190,110,30,0) 100%),
      linear-gradient(90deg, var(--leaf-deep) 0%, var(--leaf) 18%, var(--leaf-light) 40%, #e7eb9a 50%, var(--leaf-light) 62%, var(--leaf) 82%, var(--leaf-deep) 100%);
  }
  .garden-scene::after {
    content: "";
    position: absolute;
    left: 0; right: 0; bottom: 0;
    height: 260px;
    background: linear-gradient(180deg, rgba(217,154,43,0) 0%, rgba(200,130,40,0.55) 50%, rgba(138,75,18,0.8) 100%);
  }
  .title {
    position: absolute;
    margin: 0;
    font-family: "Pinyon Script", cursive;
    font-weight: 400;
    color: var(--white);
    text-shadow: 0 0 2px var(--title-edge), 1px 1px 0 var(--title-edge), -1px -1px 0 var(--title-edge), 2px 3px 4px rgba(0,0,0,0.45);
    line-height: 1;
  }
  .title-tafsir { left: 130px; top: 30px; font-size: 170px; }
  .title-of { left: 300px; top: 150px; font-size: 200px; }
  .title-surah { left: 560px; top: 290px; font-size: 92px; white-space: nowrap; }
  .teacher-label, .teacher-name {
    position: absolute;
    margin: 0;
    color: var(--orange);
    font-weight: 900;
    text-align: right;
    text-shadow: 1px 1px 2px rgba(0,0,0,0.35);
    white-space: nowrap;
  }
  .teacher-label { right: 155px; top: 386px; font-size: 29px; }
  .teacher-name { right: 155px; top: 428px; font-size: 40px; }
  .schedule {
    position: absolute;
    left: 88px;
    top: 630px;
    margin: 0;
    color: var(--white);
    font-weight: 700;
    font-size: 25px;
    line-height: 36px;
    text-shadow: 1px 1px 3px rgba(0,0,0,0.6);
  }
  .schedule span { display: block; }
  .info-band {
    position: absolute;
    left: 0; top: 761px;
    width: 1200px;
    height: 89px;
    background: var(--band);
  }
  .contact {
    position: absolute;
    left: 88px;
    top: 13px;
    margin: 0;
    color: var(--green-text);
    font-size: 13px;
    line-height: 24px;
    font-weight: 700;
  }
  .contact span { display: block; }
  .contact .detail { font-weight: 700; color: var(--green-text); opacity: 0.85; }
  .institute {
    position: absolute;
    left: 905px;
    top: 26px;
    display: flex;
    align-items: center;
    gap: 10px;
  }
  .institute-dot {
    width: 22px;
    height: 22px;
    border-radius: 50%;
    background: var(--orange);
  }
  .institute-name {
    color: var(--orange);
    font-weight: 900;
    font-size: 26px;
    white-space: nowrap;
  }
</style>
</head>
<body>
  <main class="flyer">
    <div class="garden-scene" role="img" aria-label="Sunlit tree-lined garden path in autumn light, with an open Quran resting on a carved wooden stand in the centre"></div>

    <h1 class="title title-tafsir">Tafsir</h1>
    <span class="title title-of">Of</span>
    <span class="title title-surah">Surah Maidah</span>

    <p class="teacher-label">Taught by</p>
    <p class="teacher-name">Delira Nasrim</p>

    <p class="schedule">
      <span>June 1 to June 15 2017</span>
      <span>Daily Monday thru Thursday</span>
      <span>1:30 PM to 2:30 PM</span>
    </p>

    <footer class="info-band">
      <p class="contact">
        <span>Unity Hall of Brookvale Township: <span class="detail" style="display:inline">2400 Tarrow Road | Piscataway NJ 08617</span></span>
        <span>For more information: <span class="detail" style="display:inline">sahelwing4@quorimail.com</span></span>
      </p>
      <div class="institute">
        <span class="institute-dot"></span>
        <span class="institute-name">Verse Light Institute</span>
      </div>
    </footer>
  </main>
</body>
</html>
```